A four page bi-fold A4 brochure

The words and photos are attached. We want an innovative design using www.amberwillowgroup.co.uk fonts, colours and themes and any pics which can enhance. The Copper Kite Property logo should also be used as it is a joint venture.

real estate, financial services

```html
<!DOCTYPE html>
<html lang="en">
<head>
<meta charset="utf-8">
<title>Property Investment and Sourcing Intensive Course – Brochure Spread</title>
<link href="https://fonts.googleapis.com/css2?family=Montserrat:ital,wght@0,400;0,500;0,600;0,700;0,800;1,700&display=swap" rel="stylesheet">
<style>
  :root {
    --navy: #1f2b5b;
    --deep-navy: #1b2440;
    --backdrop: #23365a;
    --crimson: #8a1428;
    --red: #b3112e;
    --ink: #2b2b2b;
    --paper: #ffffff;
    --rule: #555a66;
  }
  * { box-sizing: border-box; margin: 0; padding: 0; }
  html, body { width: 1200px; height: 1200px; overflow: hidden; }
  body {
    background: var(--backdrop);
    font-family: "Montserrat", Arial, sans-serif;
    color: var(--ink);
    position: relative;
  }
  .spread {
    position: absolute;
    left: 20px; top: 190px;
    width: 1160px; height: 820px;
    display: flex;
    box-shadow: 0 20px 50px rgba(0,0,0,.35);
  }
  .page {
    position: relative;
    width: 580px; height: 820px;
    background: var(--paper);
    overflow: hidden;
  }
  .page--left { border-right: 1px solid #d9dbe0; }
  .page-foot {
    position: absolute; left: 0; right: 0; bottom: 0; height: 30px;
    background: var(--deep-navy);
    border-top: 4px solid var(--crimson);
  }
  .abs { position: absolute; }
  .section-title {
    font-weight: 800; color: var(--navy);
    font-size: 19px; letter-spacing: 1.2px; line-height: 1.1;
    white-space: nowrap;
  }
  .lead { font-size: 10px; margin: 6px 0 8px; }
  .case {
    border-left: 2px solid var(--crimson);
    padding-left: 10px;
    font-size: 10px; line-height: 1.35;
  }
  .case p { margin-bottom: 6px; }
  .case strong { font-weight: 700; color: var(--ink); }
  .case .equity { font-weight: 700; font-style: italic; color: var(--navy); font-size: 11px; }
  .photo { border-radius: 2px; }
  .photo--mansion { background: linear-gradient(160deg, #5d7a3a 0%, #8c4a36 45%, #3f5a2a 100%); }
  .photo--terrace { background: linear-gradient(180deg, #7aa6d6 0%, #3b3f48 40%, #9a8f86 75%, #5d5a56 100%); }
  .photo--book { background: linear-gradient(150deg, #2a2d33 0%, #3a3a2e 60%, #c99a2e 100%); border-radius: 3px; box-shadow: 4px 4px 10px rgba(0,0,0,.3); }
  .photo--auction { background: linear-gradient(180deg, #f1f1f1 0%, #d8ecd6 30%, #f6f6f6 55%, #e24a3b 90%); }
  .photo--bridging { background: linear-gradient(180deg, #ffffff 0%, #efe6d8 60%, #d8b98a 100%); }
  .photo--mortgage { background: linear-gradient(160deg, #5ba3dd 0%, #9ccaf0 55%, #e9e9e9 100%); }
  .divider { height: 1px; background: var(--rule); }
  .callout { text-align: center; font-size: 10px; line-height: 1.35; }
  .callout strong { display: block; font-weight: 700; }
  .headline {
    color: var(--red); font-weight: 800; font-size: 16px; letter-spacing: .2px;
    white-space: nowrap;
  }
  .course-title {
    color: var(--navy); font-weight: 800; font-size: 16.5px; letter-spacing: .1px;
    white-space: nowrap;
  }
  .core { text-align: center; font-weight: 700; font-size: 13px; color: var(--ink); }
  .objectives { font-size: 10.5px; line-height: 1.42; }
  .objectives .item-head { font-weight: 700; }
  .tag {
    position: absolute;
    background: var(--crimson); color: #fff;
    font-size: 9px; font-weight: 700;
    padding: 4px 14px;
    white-space: nowrap;
  }
</style>
</head>
<body>
<main class="spread">

  <section class="page page--left">
    <div class="abs" style="left:30px; top:36px; width:270px;">
      <h2 class="section-title">PROPERTY INVESTORS:</h2>
      <p class="lead">We will show you how to source deals like this:</p>
      <div class="case">
        <p><strong>Apartment for £5,000 (purchased 2023)</strong></p>
        <p>In 2017, this property sold for £59,950. It could be resold now, in 2023, for up to as much as £85,000. It was purchased by us for £5,000 cash plus debt – an asset for debt swap. No refurbishment was required. Market rent is £550 pcm or £6,600.</p>
        <p class="equity">Equity c. £60,000 Yield 44%</p>
      </div>
    </div>
    <div class="abs photo photo--mansion" role="img" aria-label="Photo of a red-brick Victorian house behind a hedge and gate pillars" style="left:312px; top:40px; width:240px; height:150px;"></div>

    <div class="abs divider" style="left:30px; right:28px; top:215px;"></div>

    <h2 class="abs section-title" style="left:30px; top:230px; font-size:17px;">PROPERTY SOURCING AGENTS &amp; INVESTORS:</h2>
    <div class="abs" style="left:30px; top:250px; width:280px;">
      <p class="lead">We will show you how to source deals like this:</p>
      <div class="case">
        <p><strong>House - £90,000 (purchased 2023)</strong></p>
        <p>28% below market value. Yield 10% or 17% net as a HMO.</p>
        <p>Fee earned £4,000 plus add-ons.</p>
        <p>The same client has purchased 5 properties this year, a minimum fee income of £20,000 before add-ons from just one client.</p>
      </div>
    </div>
    <div class="abs photo photo--terrace" role="img" aria-label="Photo of a row of red-brick terraced houses with bay windows" style="left:322px; top:258px; width:232px; height:145px;"></div>

    <div class="abs callout" style="left:30px; right:28px; top:428px;">
      <strong>You can do this!</strong>
      Be a property investor AND property sourcing agent. The deals you have spent time researching and do not want, sell to others for a fee and also JV with agents to sell to their clients.
    </div>

    <div class="abs" style="left:30px; right:24px; top:486px;">
      <h1 class="headline">LEARN HOW TO BUY PROPERTY AND FLIP, USING NO CASH!</h1>
      <h2 class="course-title" style="margin-top:6px;">The Property Investment and Sourcing Intensive Course:</h2>
      <p class="core" style="margin-top:8px;">Core objectives</p>
      <div class="objectives" style="margin-top:6px;">
        <p class="item-head">1. Distressed Property Investment – Source property substantially below market value (BMV)</p>
        <p>a.&nbsp; What is a distressed asset, and why now is the best time to invest since 2008/2009.</p>
        <p>b.&nbsp; How to source BMV distressed assets for personal investment purposes or to sell on to others, either for a fee or profit (flip).</p>
        <p>c.&nbsp; Buy properties with NO CASH and flip for profit using a professional legal technique.</p>
        <p>d.&nbsp; What’s a property Call Option?</p>
        <p>e.&nbsp; Creating a viable property strategy, whether for investment, development, or sourcing.</p>
        <p>f.&nbsp; Houses v HMOs v Leasehold Flats – what’s the best strategy in the current market?</p>
        <p>g.&nbsp; Learn to value a property like a professional.</p>
        <p>h.&nbsp; Understand the key investment ratios and numbers which make a potentially good investment, OUTSTANDING.</p>
      </div>
    </div>

    <div class="page-foot"></div>
  </section>

  <section class="page page--right">
    <div class="abs objectives" style="left:28px; right:28px; top:36px;">
      <p class="item-head">2. Property Auctions – Repossessions, Bankruptcies and Bargain Properties LIVE</p>
      <p>i.&nbsp; <em style="font-weight:700;font-style:italic;">50% below market value (BMV) is achievable</em> – illustrated with real-world examples.</p>
      <p>j.&nbsp; Property Auctions – Not all properties at auction offer value. How to sort the outstanding opportunities from the duds.</p>
      <p>k.&nbsp; Property auction strategies and tactics that work in 2023.</p>
      <p>l.&nbsp; Navigate the legal pack – fix issues for a huge uplift in value – real-world examples.</p>
    </div>

    <div class="abs photo photo--book" role="img" aria-label="Photo of a dark guidebook on property auctions with gold lettering and an upward arrow" style="left:90px; top:150px; width:118px; height:168px;"></div>
    <div class="abs photo photo--auction" role="img" aria-label="Screenshot of an online auction result: Sold for £55,000, ended 24th May 2023" style="left:330px; top:160px; width:200px; height:130px;"></div>

    <div class="abs objectives" style="left:28px; right:28px; top:345px;">
      <p class="item-head">3. Off-market</p>
      <p>m.&nbsp; How to source off-market opportunities. 100% or more below market value (BMV) is achievable. Illustrated with real-world examples.</p>
      <p>n.&nbsp; Sources of Intelligence – Where do you find off-market bargains like this?</p>
    </div>
    <span class="tag" style="left:40px; top:425px;">Purchased 2023 - £17,500</span>
    <span class="tag" style="left:225px; top:418px;">Sold in 2017 for £59,950</span>
    <span class="tag" style="left:400px; top:410px;">Potential value £85,000</span>
    <span class="tag" style="left:170px; top:445px;">2-bed garden flat - £5,000 refurbishment Yield 28%</span>

    <div class="abs objectives" style="left:28px; right:28px; top:485px;">
      <p class="item-head">4. Law - how to fix problems for an instant uplift in equity</p>
      <p>o.&nbsp; The legal pitfalls to avoid and the legal challenges to embrace.</p>
      <p>p.&nbsp; Do you buy in a limited company or as an individual?</p>
      <p>q.&nbsp; How to manage risk. The risk management matrix.</p>
      <p class="item-head" style="margin-top:6px;">5. Finance – the latest bridging and mortgage advice</p>
      <p>r.&nbsp; Discover the best and most up-to-date sources of finance available. Get the latest mortgage and bridging advice from an expert, and also learn how to qualify.</p>
    </div>

    <div class="abs photo photo--bridging" role="img" aria-label="Photo of a hand placing a coin beside stacked coins and a wooden house block reading Bridging Loan" style="left:60px; top:650px; width:190px; height:120px;"></div>
    <div class="abs photo photo--mortgage" role="img" aria-label="Photo of a model house beside a small sign reading Fixed rate vs variable rate mortgage" style="left:310px; top:628px; width:236px; height:150px;"></div>

    <div class="page-foot"></div>
  </section>

</main>
</body>
</html>
```